Professional Hairdresser needs powerful, clever, simple, modern business card

I need a professional, clever, powerful, bold, attractive, modern/simplistic business card.
I specialize in dimensional hair color, precision haircutting, modern classic design, and signature finishes.
I believe in advanced education, continued training with emphasis on perfect practice, and strive to be the best at what I do.
I am trained by the industry's best and have passion for what I do, I want my business card to reflect my talents, education, capabilities, signature color techniques and design and confidence.
I want to be known as reputable, bold, artistic, aware, classic yet modern, innovative, creative, dimensional, knowledgeable, and educated.
I want something bold, simple, elegant, modern, clever, and legible.
My personal style is progressive, modern, eclectic, clean with modern luxury comfort style.
I love the use of black and white, to creative visual interest and texture. I think putting black as a solid background with white bold font makes the words jump/glow to the eye. I also think a stark white background with bold black fonts looks great, maybe with a punch of red. It is simple, clean, elegant.
I have a QR code I would like to include on the card but have no idea how to make it visually pleasing or make sense.
I do not have a set logo and am not sure if this needs to be done first or if the business card should be done first.
Updates

Reason: Very difficult decision. All designers are amazing.

Reason: Difficult decisions

Reason: Need more time as yesterday was not able to work as much as possible with designers. They are all great and look forward to having time later to look at them.

Reason: Unexpected time delay.

Target Market(s)

Early 20's-mid 60's, female and male, fashion aware, people who can afford my prices, appreciate value

Industry/Entity Type

Training

Requirements
Must have
• I would like to incorporate the QR code I have if possible.
I would like to have my name and contact info.
I would like my logo (or maybe have my logo be RT in a font like listed below).
I would like the fonts to be modern, bold, clean, readable.
Fonts I have looked at are: The font used on the book called: Morvani An Age of Bright Shapes" I really love. I have looked at glyphwell.net for font and found "Georgiquas", but the designer wanted 200 euros which I just dont have at the time. Others I looked at include "Lin Libertine", Alien-Encounters-solid-regular-italic".
I love font used in the picture I included with the Tobias.Lindqvist ad.
Clean, modern, professional, legible, structured.
Nice to have
• I envision a black background with bold, modern, simple, font in white creating the effect of the words jumping off the card, visually apparent and glowing. Like a really expensive restaurant with a sign that you cant miss because the name is in bright white on black background, simple, bold, modern but not futuristic, powerful, clever, elegant, and draws the eye making it unforgetable. Perhaps layering black and white in order to where the font will be in white.
I see balance and chic.
Perhaps
Should not have
• I appreciate the trends in business design, but realize trends come and go and not sure if having something "trendy" is advisable for me. Having said that, I like creative modern design and sometimes current trends are important in design. I do like red as accent color, the primary blue color, blue on the PixelQuorum page, the masculine/florescent purple, and the neo bold yellow and the primary color shade of yellow.
I do not want clutter.
I do not want any fonts that are swirly, old-world calligraphy, script, or penmanship style.
I do not want picture of scissors, heads of old-school beauty school hair, or barber poles.

```html
<!DOCTYPE html>
<html lang="en">
<head>
<meta charset="utf-8">
<title>Ryan Tate — Style Colorist</title>
<link rel="stylesheet" href="https://fonts.googleapis.com/css2?family=Saira+Condensed:wght@200;300&display=swap">
<style>
  :root {
    --card-bg-start: #232325;
    --card-bg-end: #141318;
    --frame: #2a2f3a;
    --phone-gold: #f7cf73;
    --role-blue: #8fd3f5;
    --name-white: #f4f4f4;
    --city-grey: #6e6e72;
    --emblem-navy: rgba(24, 26, 70, 0.85);
    --emblem-magenta: rgba(170, 20, 180, 0.55);
    --emblem-gold: rgba(240, 180, 50, 0.45);
  }
  * { margin: 0; padding: 0; box-sizing: border-box; }
  html, body {
    width: 1200px;
    height: 733px;
    overflow: hidden;
    background: #0e0e10;
  }
  .card {
    position: relative;
    width: 1200px;
    height: 733px;
    overflow: hidden;
    background: linear-gradient(135deg, var(--card-bg-start) 0%, var(--card-bg-end) 100%);
    border: 3px solid var(--frame);
    font-family: "Saira Condensed", "Arial Narrow", sans-serif;
  }
  .phone {
    position: absolute;
    left: 46px;
    top: 28px;
    font-size: 118px;
    font-weight: 200;
    letter-spacing: 8px;
    color: var(--phone-gold);
    line-height: 1;
  }
  .role {
    position: absolute;
    left: 136px;
    top: 216px;
    font-size: 54px;
    font-weight: 300;
    line-height: 0.95;
    color: var(--role-blue);
  }
  .name {
    position: absolute;
    left: 74px;
    top: 360px;
    font-size: 140px;
    font-weight: 200;
    letter-spacing: 12px;
    color: var(--name-white);
    line-height: 1;
  }
  .cities {
    position: absolute;
    left: 0;
    top: 574px;
    width: 100%;
    font-size: 54px;
    font-weight: 300;
    letter-spacing: 3px;
    color: var(--city-grey);
    line-height: 1;
  }
  .cities span { position: absolute; }
  .city-orlando { left: 112px; }
  .city-miami { left: 563px; }
  .city-milan { left: 975px; }
  .emblem {
    position: absolute;
    left: 770px;
    top: 100px;
    width: 370px;
    height: 400px;
    border-radius: 50%;
    background:
      radial-gradient(circle at 45% 30%, var(--emblem-navy) 0%, rgba(24, 26, 70, 0) 55%),
      radial-gradient(ellipse at 55% 80%, var(--emblem-magenta) 0%, rgba(170, 20, 180, 0) 50%),
      radial-gradient(ellipse at 80% 75%, var(--emblem-gold) 0%, rgba(240, 180, 50, 0) 40%);
  }
</style>
</head>
<body>
  <main class="card">
    <div class="emblem" role="img" aria-label="Signature emblem: blue arc over a magenta and gold check mark"></div>

    <div class="phone">483 555-0172</div>
    <div class="role">style<br>colorist</div>
    <h1 class="name">RYAN TATE</h1>
    <div class="cities">
      <span class="city-orlando">orlando</span>
      <span class="city-miami">miami</span>
      <span class="city-milan">milan</span>
    </div>
  </main>
</body>
</html>
```